Luxury and organic beauty products need a Design

We need a bottle and packaging design for a new business in New Zealand, called Kelvara Botanicals. We are creating a selection of Luxury and premium products to have at the Kelvara luxury villa's (www.kelvaraluxuryvilla.com), as well to sell online and at boutique stores.

The products are: Body wash, Shampoo, Conditioner, Hand wash, Body lotion, Air fresheners and Bath salts.

We would like to use the Kelvara Botanicals logo in Silver as Kelvara Luxury Villa's a having it in Gold, so it separates the two products. Also the packaging will be Navy Blue along with the silver.

The final design should be sleek, sophisticated and have a luxury feel. Our customers will have the product in the bathroom and kitchen so the bottles must be proud to show off. " This should look and feel like a very high end product.

Boxes will have embossed writing (logo) and a slightly textured feel or look.

Please find attached images of some examples to use for inspiration only.

Target Market(s)

Luxury boutique villas, Boutique stores, High end stores

Industry/Entity Type

Personal and hair care

Colors
0054AA
0677BA
7BADD7
CADEEF
E8F1F8
FFC000
F8CF3A
FAE287
FDF2CF
FEFAEE

Requirements
Must have
• Use the provided Logo, look and feel luxurious, but at the same time organic
Nice to have
• A bottle that reminds precious stones. I have just attached an example
Should not have
• Dark colour, heavy fonts

```html
<!DOCTYPE html>
<html lang="en">
<head>
<meta charset="utf-8">
<title>Kelvara Botanicals – Label Range</title>
<link href="https://fonts.googleapis.com/css2?family=Open+Sans:wght@400;600;700&display=swap" rel="stylesheet">
<style>
  :root {
    --bg: #ececec;
    --ink: #3f3f3f;
    --ink-soft: #5a5a5a;
    --shampoo: #5aa6cc;
    --conditioner: #3fd6a6;
    --handwash: #d4b02e;
    --gold: #c99a2e;
    --band-light: #f6f8f8;
    --band-steel: #c9d6da;
    --band-teal: #a9bfc0;
    --leaf: #d6d6d6;
  }
  * { margin: 0; padding: 0; box-sizing: border-box; }
  html, body { width: 1200px; height: 848px; overflow: hidden; }
  body {
    font-family: "Open Sans", sans-serif;
    color: var(--ink);
    background: linear-gradient(180deg, #f1f1f1 0%, var(--bg) 60%, #e6e6e6 100%);
    position: relative;
  }
  .botanical-art {
    position: absolute;
    border-radius: 50%;
    background: radial-gradient(ellipse at center, rgba(200,200,200,.45) 0%, rgba(220,220,220,.2) 55%, rgba(236,236,236,0) 75%);
  }
  .botanical-art.top { left: 450px; top: -20px; width: 300px; height: 160px; }
  .botanical-art.bottom { left: 450px; top: 680px; width: 250px; height: 180px; }

  .brand-header { position: absolute; left: 0; width: 1200px; top: 114px; text-align: center; padding-left: 170px; }
  .brand-header .name { font-weight: 700; font-size: 38px; letter-spacing: 6px; color: var(--ink); line-height: 45px; }
  .brand-header .sub { margin-top: 12px; font-size: 20px; letter-spacing: 8px; color: var(--ink); }

  .label-band {
    position: absolute; left: 0; top: 378px; width: 1200px; height: 288px;
    background: linear-gradient(90deg, #ffffff 0%, var(--band-light) 12%, var(--band-steel) 20%, var(--band-light) 30%, #e4eaec 45%, var(--band-light) 58%, #e8eef0 72%, var(--band-light) 84%, var(--band-teal) 100%);
  }

  .side-panel { position: absolute; top: 26px; height: 236px; display: flex; gap: 10px; }
  .ingredients-text {
    writing-mode: vertical-rl; font-size: 5.6px; letter-spacing: 1.1px; line-height: 7.4px;
    color: var(--ink-soft); height: 236px; width: 46px; overflow: hidden;
  }
  .ingredients-title { writing-mode: vertical-rl; font-size: 7px; letter-spacing: 1px; color: var(--ink-soft); }
  .values-line { writing-mode: vertical-rl; font-size: 8.5px; letter-spacing: 1.6px; margin-left: 18px; }

  .product-label { position: absolute; width: 220px; text-align: center; }
  .product-label .name { font-weight: 700; font-size: 20px; letter-spacing: 3px; color: var(--ink); line-height: 24px; }
  .product-label .sub { font-size: 10.5px; letter-spacing: 3.5px; margin-top: 6px; color: var(--ink); }
  .product-label .product { font-size: 23px; letter-spacing: 3px; margin-top: 4px; line-height: 28px; }
  .product-label .claim { font-size: 7.4px; letter-spacing: .8px; line-height: 9.5px; margin-top: 9px; color: var(--ink-soft); }
  .product-label .maker { margin-top: 28px; display: flex; justify-content: center; align-items: center; gap: 5px; color: var(--gold); font-size: 10px; font-weight: 600; letter-spacing: 1px; }
  .product-label .maker .dot { width: 9px; height: 9px; border-radius: 50%; border: 1px solid var(--gold); }
  .product-label .origin { margin-top: 22px; font-size: 5px; font-weight: 700; letter-spacing: 1.4px; line-height: 8px; color: var(--ink); }
  .label-ornament { height: 26px; margin: 0 auto 6px; width: 120px; border-radius: 50%; background: radial-gradient(ellipse, rgba(190,190,190,.4), rgba(200,200,200,0) 70%); }

  .volume { position: absolute; font-size: 8px; color: var(--ink); }

  .shampoo .product, .shampoo-line { color: var(--shampoo); }
  .conditioner .product, .conditioner-line { color: var(--conditioner); }
  .handwash .product, .handwash-line { color: var(--handwash); }

  .footer-values { position: absolute; top: 760px; left: 0; width: 1200px; padding-left: 168px; text-align: center; font-size: 13px; letter-spacing: 2.4px; color: var(--ink); }
</style>
</head>
<body>
  <div class="botanical-art top" role="img" aria-label="Faint botanical leaf sprig decoration"></div>

  <header class="brand-header">
    <div class="name">KELVARA</div>
    <div class="sub">BOTANICALS</div>
  </header>

  <section class="label-band">
    <div class="side-panel" style="left:54px">
      <p class="ingredients-text">Lorem ipsum dolor sit amet consectetuer odio non tellus natoque accumsan. Sed hac enim lorem tempus tortor justo eget scelerisque sed morbi. Senectus urna vestibulum tincidunt turpis sem magna. Nam hendrerit vitae nibh. Auctor sed urna dignissim malesuada eleifend ultrices justo. Curabitur maecenas orci.</p>
      <p class="ingredients-title">INGREDIENTS:</p>
      <p class="values-line shampoo-line">AUTHENTICITY. SUSTAINABILITY. INTEGRITY</p>
    </div>

    <div class="product-label shampoo" style="left:196px; top:14px">
      <div class="label-ornament" role="img" aria-label="Small botanical sprig ornament"></div>
      <div class="name">KELVARA</div>
      <div class="sub">BOTANICALS</div>
      <div class="product">SHAMPOO</div>
      <p class="claim">Clinically proven,<br>highly effective pure botanicals<br>for hair, body &amp; soul</p>
      <div class="maker"><span class="dot"></span>KELVARA</div>
      <p class="origin">CLEAN BEAUTY,<br>MADE OF NEW ZEALAND</p>
    </div>
    <span class="volume" style="left:382px; top:70px">250ml</span>
    <span class="volume" style="left:382px; top:238px">8.5fl oz</span>

    <div class="side-panel" style="left:458px">
      <p class="ingredients-text">Lorem ipsum dolor sit amet consectetuer odio non tellus natoque accumsan. Sed hac enim lorem tempus tortor justo eget scelerisque sed morbi. Senectus urna vestibulum tincidunt turpis sem magna. Nam hendrerit vitae nibh. Auctor sed urna dignissim malesuada eleifend ultrices justo. Curabitur maecenas orci.</p>
      <p class="ingredients-title">INGREDIENTS:</p>
      <p class="values-line conditioner-line">AUTHENTICITY. SUSTAINABILITY. INTEGRITY</p>
    </div>

    <div class="product-label conditioner" style="left:586px; top:0px">
      <div class="label-ornament" role="img" aria-label="Small botanical sprig ornament"></div>
      <div class="name">KELVARA</div>
      <div class="sub">BOTANICALS</div>
      <div class="product">CONDITIONER</div>
      <p class="claim">Clinically proven,<br>highly effective pure botanicals<br>for hair, body &amp; soul</p>
      <div class="maker"><span class="dot"></span>KELVARA</div>
      <p class="origin">CLEAN BEAUTY,<br>MADE OF NEW ZEALAND</p>
    </div>
    <span class="volume" style="left:772px; top:54px">250ml</span>
    <span class="volume" style="left:772px; top:222px">8.5fl oz</span>

    <div class="side-panel" style="left:838px">
      <p class="ingredients-text">Lorem ipsum dolor sit amet consectetuer odio non tellus natoque accumsan. Sed hac enim lorem tempus tortor justo eget scelerisque sed morbi. Senectus urna vestibulum tincidunt turpis sem magna. Nam hendrerit vitae nibh. Auctor sed urna dignissim malesuada eleifend ultrices justo. Curabitur maecenas orci.</p>
      <p class="ingredients-title">INGREDIENTS:</p>
      <p class="values-line handwash-line">AUTHENTICITY. SUSTAINABILITY. INTEGRITY</p>
    </div>

    <div class="product-label handwash" style="left:967px; top:0px">
      <div class="label-ornament" role="img" aria-label="Small botanical sprig ornament"></div>
      <div class="name">KELVARA</div>
      <div class="sub">BOTANICALS</div>
      <div class="product">HANDWASH</div>
      <p class="claim">Clinically proven,<br>highly effective pure botanicals<br>for hair, body &amp; soul</p>
      <div class="maker"><span class="dot"></span>KELVARA</div>
      <p class="origin">CLEAN BEAUTY,<br>MADE OF NEW ZEALAND</p>
    </div>
    <span class="volume" style="left:1152px; top:54px">250ml</span>
    <span class="volume" style="left:1152px; top:222px">8.5fl oz</span>
  </section>

  <div class="botanical-art bottom" role="img" aria-label="Faint botanical leaf sprig decoration"></div>

  <p class="footer-values">AUTHENTICITY. SUSTAINABILITY. INTEGRITY</p>
</body>
</html>
```